Business Card and stationary project for Nutrition Consulitng Company
QV Nutrition Consulting, PC
Business Card and stationary project for Nutrition Consulitng Company - Health
Creative Brief
Bright & Fun-filled
leave adjustable for each staff
5182 27th Ave. Suite 100 Alder Falls, WY 68457
leave adjustable
rmalden@qvnutritionconsulting.example
www.qvnutritionconsulting.example
I would like the business cards to be editable for each staff member. This would include name, title, cell number, and email address.
please address my website www.qvnutriitionconsulting.example for ideas, as well as the uploaded logo and letter head

```html
<!DOCTYPE html>
<html lang="en">
<head>
<meta charset="utf-8">
<title>QV Nutrition Consulting, PC – Business Cards</title>
<link href="https://fonts.googleapis.com/css2?family=Tinos:ital,wght@0,400;0,700;1,400&display=swap" rel="stylesheet">
<style>
  :root {
    --backdrop: #e7e4e1;
    --card-white: #ffffff;
    --card-brown: #6e3c22;
    --band-brown: #70402a;
    --band-stripe: #8a5a40;
    --text-brown: #5a321e;
    --text-grey: #4a4a4a;
    --accent-orange: #e8701c;
    --footer-grey: #efeeec;
  }
  * { box-sizing: border-box; margin: 0; padding: 0; }
  html, body { width: 1200px; height: 869px; overflow: hidden; }
  body {
    background: var(--backdrop);
    font-family: "Tinos", "Times New Roman", serif;
    position: relative;
  }
  .card {
    position: absolute;
    border-radius: 14px;
    overflow: hidden;
    box-shadow: 0 8px 22px rgba(0,0,0,.18);
  }
  /* Front */
  .card-front {
    left: 320px; top: 48px; width: 560px; height: 320px;
    background: var(--card-white);
  }
  .front-band {
    position: absolute; left: 0; right: 0; top: 42px; height: 88px;
    background: var(--band-brown);
    border-top: 4px solid var(--band-stripe);
    border-bottom: 4px solid var(--band-stripe);
  }
  .holder { position: absolute; left: 306px; top: 56px; color: #fff; }
  .holder-name { font-size: 22px; font-weight: 700; }
  .holder-title { font-size: 14px; margin-top: 4px; }
  .brand-name {
    position: absolute;
    color: var(--text-brown);
    font-weight: 700;
    white-space: nowrap;
    line-height: 1.1;
  }
  .front-brand { left: 22px; top: 176px; font-size: 18px; }
  .tagline {
    position: absolute; left: 22px; top: 206px;
    font-size: 9.5px; font-style: italic; color: var(--accent-orange);
    white-space: nowrap;
  }
  .contact {
    position: absolute; left: 306px; top: 146px;
    font-size: 10.5px; line-height: 1.45; color: var(--text-grey);
    white-space: nowrap;
  }
  .contact .gap { height: 8px; }
  .front-footer {
    position: absolute; left: 0; right: 0; bottom: 0; height: 46px;
    background: var(--footer-grey);
    border-top: 3px solid var(--band-brown);
    display: flex; align-items: center; justify-content: center;
    font-size: 12px; letter-spacing: 2px; color: var(--text-brown);
  }
  /* Backs */
  .card-back { top: 452px; width: 520px; height: 330px; }
  .back-white { left: 50px; background: var(--card-white); }
  .back-brown { left: 630px; background: var(--card-brown); }
  .back-brand { left: 60px; top: 140px; font-size: 28px; }
  .back-brown .brand-name { color: #fff; }
  .back-web {
    position: absolute; left: 60px; bottom: 40px;
    font-size: 13px; letter-spacing: 1.5px; color: var(--text-brown);
    white-space: nowrap;
  }
  .back-brown .back-web { color: #f3e6dc; }
</style>
</head>
<body>

  <section class="card card-front" aria-label="Business card front">
    <div class="front-band"></div>
    <div class="holder">
      <div class="holder-name">Your Name</div>
      <div class="holder-title">Title</div>
    </div>
    <span class="brand-name front-brand">QV Nutrition Consulting, PC</span>
    <p class="tagline">Simple steps toward balanced, everyday wellness</p>
    <div class="contact">
      <div>5182 27th Ave. Suite 210</div>
      <div>Alder Falls, WY 68457</div>
      <div class="gap"></div>
      <div>Phone: 555-201-0142</div>
      <div>Cell: 555-201-0178</div>
      <div>Fax: 555-201-0193</div>
      <div>Email: rmalden@qvnutritionconsulting.example</div>
    </div>
    <div class="front-footer">www.qvnutritionconsulting.example</div>
  </section>

  <section class="card card-back back-white" aria-label="Business card back, white">
    <span class="brand-name back-brand">QV Nutrition Consulting, PC</span>
    <div class="back-web">www.qvnutritionconsulting.example</div>
  </section>

  <section class="card card-back back-brown" aria-label="Business card back, brown">
    <span class="brand-name back-brand">QV Nutrition Consulting, PC</span>
    <div class="back-web">www.qvnutritionconsulting.example</div>
  </section>

</body>
</html>
```